Business Card Design

Electronic Security
Alarm Systems
CCTV
Electronic Access Control
Security System Integration

Industry/Entity Type

Business

Contact Information for Business Card

Gareth Linwood
PO Box 862
Yarrowdale Qld 4173
Phone 07 38265140
Mob 0428637291

```html
<!DOCTYPE html>
<html lang="en">
<head>
<meta charset="utf-8">
<title>Halden – Business Card</title>
<link href="https://fonts.googleapis.com/css2?family=Arimo:wght@400;700&display=swap" rel="stylesheet">
<style>
  :root {
    --bg-light: #e4e4e4;
    --bg-dark: #a9a9a9;
    --card: #ffffff;
    --ink: #1b1b1f;
    --brand-ink: #23262e;
    --blue: #1aa3dd;
    --slate: #2c3a46;
    --orange: #f07a2a;
    --yellow: #ffc21a;
  }
  * { margin: 0; padding: 0; box-sizing: border-box; }
  html, body {
    width: 1200px;
    height: 1170px;
    overflow: hidden;
  }
  body {
    background: radial-gradient(ellipse at 50% 30%, var(--bg-light) 0%, var(--bg-dark) 100%);
    font-family: "Arimo", Arial, sans-serif;
    color: var(--ink);
    position: relative;
  }
  .card {
    position: absolute;
    left: 100px;
    top: 285px;
    width: 1000px;
    height: 600px;
    background: var(--card);
    box-shadow: 0 6px 18px rgba(0,0,0,0.28);
    overflow: hidden;
  }
  .card-art {
    position: absolute;
    inset: 0;
    width: 100%;
    height: 100%;
  }
  .brand {
    position: absolute;
    left: 0;
    right: 0;
    top: 290px;
    display: flex;
    justify-content: center;
    align-items: center;
    gap: 16px;
  }
  .brand-mark {
    width: 34px;
    height: 34px;
    background: var(--brand-ink);
  }
  .brand-name {
    font-size: 56px;
    font-weight: 400;
    letter-spacing: 2px;
    color: var(--brand-ink);
  }
  .contact {
    position: absolute;
    left: 62px;
    bottom: 42px;
    font-size: 22px;
    line-height: 31px;
  }
  .contact strong { font-weight: 700; }
  .services {
    position: absolute;
    right: 58px;
    bottom: 82px;
    list-style: none;
    text-align: right;
    font-size: 24px;
    line-height: 30px;
  }
</style>
</head>
<body>
  <article class="card">
    <svg class="card-art" viewBox="0 0 1000 600" preserveAspectRatio="none">
      <defs>
        <linearGradient id="facet-blue" x1="0" y1="0" x2="1" y2="1">
          <stop offset="0" stop-color="var(--slate)"/>
          <stop offset="0.5" stop-color="var(--blue)"/>
          <stop offset="1" stop-color="var(--slate)"/>
        </linearGradient>
        <linearGradient id="facet-orange" x1="0" y1="0" x2="1" y2="1">
          <stop offset="0" stop-color="var(--yellow)"/>
          <stop offset="1" stop-color="var(--orange)"/>
        </linearGradient>
      </defs>
      <polygon role="img" aria-label="Blue faceted corner decoration"
               fill="url(#facet-blue)"
               points="0,0 420,0 350,48 170,48 0,330"/>
      <polygon role="img" aria-label="Orange faceted corner decoration"
               fill="url(#facet-orange)"
               points="790,0 1000,0 1000,250 965,120 880,50"/>
    </svg>

    <div class="brand">
      <span class="brand-mark"></span>
      <span class="brand-name">HALDEN</span>
    </div>

    <address class="contact" style="font-style: normal;">
      <div><strong>Address:</strong> Gareth Linwood</div>
      <div>PO Box 862</div>
      <div>Yarrowdale Qld 4173</div>
      <div><strong>Phone:</strong> 07 38265140</div>
      <div><strong>Mob:</strong> 0428637291</div>
    </address>

    <ul class="services">
      <li>Electronic Security</li>
      <li>Alarm Systems</li>
      <li>CCTV</li>
      <li>Electronic Access Control</li>
      <li>Security System Integration</li>
    </ul>
  </article>
</body>
</html>
```